Einfache Webside für kleine Promotion- und Personalagentur
Zielgruppe
Lumo Staffing ist eine international tätige Promotion- und Personalagentur. Wir bieten auch im Bereich Sport der jew. Sportart affine Hostessen und Hosts f an.
Aufgabenstellung
Wir hatten bis dato eine sehr gute Auftragslage und leider keine Zeit für eine Homepage. Wir suchen jemaden der uns das Design für die Seite übernimmt und Online stellt. Wir sind auch offen wenn dies über z.B. Q+Z erfolgt. Auf den jeweiligen Seiten wollen wir den Text dann immer selbst eintragen. Seiten: Startseite mit Buttons zu folgenden Feldern: Promotion (Text mit Erklärung was wir machen und Bildern), Personal (Text mit Erklärung was wir machen und Bilder - die Bilder sollten austauschbar sein), Team, Referenzen, Kontaktseite, Gästebuch, Impressum. Die Seite sollte Modern aussehen und nicht zu überladen sein.

```html
<!DOCTYPE html>
<html lang="de">
<head>
<meta charset="utf-8">
<title>Lumo Staffing – International Promotion &amp; HR services</title>
<link rel="stylesheet" href="https://fonts.googleapis.com/css2?family=Lato:wght@400;700&display=swap">
<style>
  :root {
    --teal: #7ccdd6;
    --teal-strong: #5fc0cc;
    --slate: #8a969c;
    --ink: #1d1d1f;
    --muted: #4d565b;
    --white: #ffffff;
    --sky-1: #eef4f9;
    --sky-2: #d9e6f1;
  }
  * { box-sizing: border-box; margin: 0; padding: 0; }
  html, body { width: 1200px; height: 831px; overflow: hidden; background: var(--white); }
  body { position: relative; font-family: "Lato", sans-serif; color: var(--ink); }

  .site-header {
    position: absolute; left: 0; top: 0; width: 1200px; height: 286px;
    background: linear-gradient(180deg, var(--sky-1) 0%, var(--sky-2) 100%);
  }

  .utility-nav {
    position: absolute; top: 24px; left: 886px;
    font-size: 14px; color: var(--muted); letter-spacing: .3px;
    display: flex; align-items: center; gap: 8px;
  }
  .utility-nav svg { width: 13px; height: 13px; }

  .brand {
    position: absolute; left: 0; width: 1200px; top: 48px;
    display: flex; flex-direction: column; align-items: center;
  }
  .brand-dot {
    width: 96px; height: 96px; border-radius: 50%; background: var(--slate);
  }
  .brand-name {
    margin-top: 22px; font-size: 42px; font-weight: 400; color: var(--slate);
    letter-spacing: .5px; line-height: 1;
  }
  .brand-tagline {
    margin-top: 8px; font-size: 15.5px; color: var(--slate); letter-spacing: .3px;
  }

  .main-nav {
    position: absolute; left: 0; top: 286px; width: 1200px; height: 44px;
    background: var(--teal);
  }
  .main-nav a {
    position: absolute; top: 12px; transform: translateX(-50%);
    font-size: 15.5px; letter-spacing: 1.2px; color: #1f2a2e; text-decoration: none;
    white-space: nowrap;
  }

  .service {
    position: absolute; top: 362px; width: 260px; margin-left: -130px;
    display: flex; flex-direction: column; align-items: center;
  }
  .service h2 { font-size: 18.5px; font-weight: 400; letter-spacing: .3px; line-height: 1.4; white-space: nowrap; }
  .service-photo {
    margin-top: 12px; width: 198px; height: 204px; border-radius: 50%;
  }
  .photo-promo { background: linear-gradient(160deg, #8a6a58 0%, #5a4440 100%); }
  .photo-hr { background: linear-gradient(160deg, #c9a57e 0%, #8a6a54 100%); }
  .photo-hostess { background: linear-gradient(160deg, #a9aaab 0%, #7f7a72 100%); }

  .service-text {
    margin-top: 38px; width: 250px; font-size: 13px; line-height: 15.5px;
    color: var(--ink);
  }
  .service-text .justified { text-align: justify; }
  .service-text p + p { margin-top: 15.5px; }
  .service-text .line { display: block; white-space: nowrap; }
  .more-button {
    margin-top: 16px; height: 27px; padding: 0 10px;
    display: flex; align-items: center; gap: 4px;
    background: var(--teal-strong); color: var(--white);
    font-size: 13px; font-weight: 700; letter-spacing: .4px; text-decoration: none;
  }
  .more-button svg { width: 12px; height: 12px; }
</style>
</head>
<body>
  <header class="site-header" role="img" aria-label="Headerfoto: Geschäftsleute in Bewegung, hellblau getönt"></header>

  <nav class="utility-nav">
    <span>Kontakt</span><span>|</span><span>Impressum</span><span>|</span>
    <svg viewBox="0 0 16 16" aria-label="Suche"><circle cx="6.5" cy="6.5" r="5" fill="none" stroke="#4d565b" stroke-width="2"/><line x1="10.3" y1="10.3" x2="15" y2="15" stroke="#4d565b" stroke-width="2.4"/></svg>
  </nav>

  <div class="brand">
    <div class="brand-dot"></div>
    <div class="brand-name">Lumo Staffing</div>
    <div class="brand-tagline">International Promotion &amp; HR services</div>
  </div>

  <nav class="main-nav">
    <a href="#" style="left:294px">STARTSEITE</a>
    <a href="#" style="left:462px">PROMOTION</a>
    <a href="#" style="left:613px">PERSONAL</a>
    <a href="#" style="left:735px">TEAM</a>
    <a href="#" style="left:864px">REFERENZEN</a>
    <a href="#" style="left:1020px">GÄSTEBUCH</a>
  </nav>

  <section class="service" style="left:274px">
    <h2>PROMOTION</h2>
    <div class="service-photo photo-promo" role="img" aria-label="Foto: Promoterin verteilt Flyer vor einem Geschäft"></div>
    <div class="service-text">
      <p class="justified">Lorem ipsum dolor sit amet, consectetuer adipiscing elit. Aenean commodo ligula eget dolor.</p>
      <p><span class="line">Aenean massa. Cum sociis natoque penati-</span><span class="line">bus et magnis dis parturient montes, nasce-</span></p>
    </div>
    <a class="more-button" href="#"><svg viewBox="0 0 12 12"><circle cx="6" cy="6" r="6" fill="#fff"/><path d="M4.5 3 7.5 6 4.5 9" fill="none" stroke="#5fc0cc" stroke-width="1.8"/></svg>MEHR INFOS</a>
  </section>

  <section class="service" style="left:605px">
    <h2>HR-SERVICE</h2>
    <div class="service-photo photo-hr" role="img" aria-label="Foto: Porträt einer Geschäftsfrau im hellen Blazer"></div>
    <div class="service-text">
      <p class="justified">Lorem ipsum dolor sit amet, consectetuer adipiscing elit. Aenean commodo ligula eget dolor.</p>
      <p><span class="line">Aenean massa. Cum sociis natoque penati-</span><span class="line">bus et magnis dis parturient montes, nasce-</span></p>
    </div>
    <a class="more-button" href="#"><svg viewBox="0 0 12 12"><circle cx="6" cy="6" r="6" fill="#fff"/><path d="M4.5 3 7.5 6 4.5 9" fill="none" stroke="#5fc0cc" stroke-width="1.8"/></svg>MEHR INFOS</a>
  </section>

  <section class="service" style="left:937px">
    <h2>MESSE-HOSTESSEN</h2>
    <div class="service-photo photo-hostess" role="img" aria-label="Foto: Zwei Hostessen in grauen Uniformen"></div>
    <div class="service-text">
      <p class="justified">Lorem ipsum dolor sit amet, consectetuer adipiscing elit. Aenean commodo ligula eget dolor.</p>
      <p><span class="line">Aenean massa. Cum sociis natoque penati-</span><span class="line">bus et magnis dis parturient montes, nasce-</span></p>
    </div>
    <a class="more-button" href="#"><svg viewBox="0 0 12 12"><circle cx="6" cy="6" r="6" fill="#fff"/><path d="M4.5 3 7.5 6 4.5 9" fill="none" stroke="#5fc0cc" stroke-width="1.8"/></svg>MEHR INFOS</a>
  </section>
</body>
</html>
```